Design & Build a Website with Wordpress for an international consulting company. Please read the details in the attached carefully.

I will be pleased to answer any questions you may have.

Thank you.

Thank you.

Thank you.
Updates

Hi, the home page shall have a placement for newsletter signup too. Thank you. Added Wednesday, March 9, 2016

Target Market(s)

US EU

Industry/Entity Type

Business Consultant

Font styles to use
Sans Serif

Requirements
Must have
• Coinvale portal, wordpress, responsive, accommodating the logo (download from the current site).
Nice to have
• professional, simple and elegant design

```html
<!DOCTYPE html>
<html lang="en">
<head>
<meta charset="utf-8">
<title>Marevio International</title>
<link href="https://fonts.googleapis.com/css2?family=Open+Sans:wght@400;600;700;800&display=swap" rel="stylesheet">
<style>
:root{
  --orange:#e8541e;
  --ink:#2e2e2e;
  --text:#777;
  --light:#f0f0f0;
  --footer:#2f2f2f;
  --footer-deep:#232323;
  --white:#fff;
}
*{box-sizing:border-box;margin:0;padding:0}
html,body{width:1200px;height:3576px;overflow:hidden}
body{font-family:"Open Sans",Arial,sans-serif;color:var(--ink);background:var(--white)}
section,header,footer{overflow:hidden}
.accent{color:var(--orange)}
.section-title{font-size:30px;font-weight:700;text-align:center;letter-spacing:.5px;line-height:40px}
.section-title::after{content:"";display:block;width:60px;height:3px;background:var(--orange);margin:12px auto 0}

/* header */
.site-header{height:120px;display:flex;align-items:center;justify-content:space-between;padding:0 88px}
.brand{display:flex;align-items:center;gap:10px;font-size:30px;font-weight:800;color:var(--orange);letter-spacing:1px}
.brand-mark{width:22px;height:22px;background:var(--orange);border-radius:50%}
.main-nav{display:flex;gap:30px;font-size:15px;font-weight:600;color:#666}
.main-nav a{color:inherit;text-decoration:none}
.main-nav .active{color:var(--orange)}

/* hero */
.hero{position:relative;height:570px;background:linear-gradient(180deg,#4f7fa8 0%,#8fb4d2 55%,#c9dceb 100%)}
.hero-photo{position:absolute;right:120px;top:0;width:520px;height:570px;background:radial-gradient(ellipse at 60% 55%,#e9eef3 0%,rgba(200,215,230,.4) 50%,rgba(200,215,230,0) 75%)}
.hero-copy{position:absolute;left:88px;top:300px;color:var(--white)}
.hero-copy h2{font-size:38px;font-weight:800;margin-bottom:14px}
.hero-copy li{list-style:none;font-size:17px;line-height:34px;display:flex;align-items:center;gap:10px}
.slider-arrows{position:absolute;right:24px;bottom:24px;display:flex;gap:6px}
.slider-arrows span{width:30px;height:30px;border-radius:50%;background:rgba(40,40,40,.7);display:flex;align-items:center;justify-content:center}

/* welcome */
.welcome{height:300px;padding:56px 88px 0;text-align:center}
.welcome p{margin-top:24px;font-size:13px;line-height:21px;color:var(--text)}

/* services */
.services{height:730px;background:var(--light);padding-top:56px}
.service-grid{display:grid;grid-template-columns:repeat(3,1fr);width:1000px;margin:60px auto 0;row-gap:60px}
.service{text-align:center;padding:0 40px}
.service-icon{width:84px;height:84px;border-radius:50%;background:var(--orange);margin:0 auto 22px;display:flex;align-items:center;justify-content:center}
.service h3{font-size:15px;font-weight:700;margin-bottom:10px}
.service p{font-size:13px;line-height:20px;color:#999}

/* blog */
.blog{height:460px;padding-top:50px}
.blog-grid{display:flex;gap:40px;margin:34px 0 0 88px}
.post{width:312px}
.post-image{position:relative;height:190px;background:linear-gradient(135deg,#cfd3d8,#7e8a96)}
.post-date{position:absolute;right:0;top:36px;width:56px;text-align:center;color:var(--white);font-weight:700}
.post-date .day{display:block;background:#3a3a3a;font-size:22px;padding:6px 0}
.post-date .year{display:block;background:var(--orange);font-size:12px;padding:4px 0}
.post h4{font-size:15px;font-weight:600;margin:14px 0 6px}
.post p{font-size:12px;line-height:18px;color:#999}

/* feature */
.feature{height:380px;background:linear-gradient(90deg,#fafafa,#ececec);display:flex;align-items:center;padding:0 88px;gap:60px}
.monitor{width:432px;flex:none}
.monitor-screen{height:236px;border:14px solid #1c1c1c;background:linear-gradient(135deg,#e7e3dc,#9aa4ae)}
.monitor-stand{width:80px;height:30px;background:#bbb;margin:0 auto}
.monitor-base{width:180px;height:8px;background:#999;margin:0 auto;border-radius:4px}
.feature-copy h2{font-size:28px;font-weight:700}
.feature-copy h2::after{content:"";display:block;width:60px;height:3px;background:var(--orange);margin-top:10px}
.feature-copy p{font-size:13px;line-height:21px;color:var(--text);margin-top:16px}
.btn-outline{display:inline-block;margin-top:20px;border:1px solid #888;padding:8px 18px;font-size:13px;color:var(--ink)}

/* products */
.products{height:480px;padding-top:40px;text-align:center}
.products .lead{font-size:14px;color:var(--text);margin-top:18px}
.product-row{display:flex;margin-top:40px}
.product{position:relative;width:300px;height:300px}
.product:nth-child(1){background:linear-gradient(135deg,#d9d2c6,#8c7f70)}
.product:nth-child(2){background:linear-gradient(135deg,#efe6d8,#b7a589)}
.product:nth-child(3){background:linear-gradient(135deg,#c9ccd0,#6f7781)}
.product:nth-child(4){background:linear-gradient(135deg,#b9413a,#3a3d48)}
.product span{position:absolute;left:0;right:0;bottom:0;padding:12px;background:rgba(20,20,20,.6);color:var(--white);font-size:13px;font-weight:600}

/* newsletter */
.newsletter{height:120px;background:var(--orange);display:flex;align-items:center;padding:0 88px;gap:24px;color:var(--white)}
.newsletter-title{white-space:nowrap}
.newsletter-title h3{font-size:24px;font-weight:700;line-height:30px}
.newsletter-title p{font-size:13px}
.field{width:260px;height:56px;background:var(--white);color:#999;font-size:14px;display:flex;align-items:center;padding:0 18px}
.newsletter .field:first-of-type{margin-left:20px}
.btn-submit{height:56px;padding:0 34px;background:#2b2b2b;color:var(--white);font-weight:700;font-size:15px;display:flex;align-items:center}

/* partners */
.partners{height:120px;display:flex;align-items:center;justify-content:space-around;padding:0 60px}
.partners span{font-size:26px;font-weight:700;color:#a7a7a7}

/* footer */
.site-footer{height:256px;background:var(--footer);display:grid;grid-template-columns:340px 200px 240px 220px;gap:30px;padding:40px 88px 0;color:#bbb;font-size:12px;line-height:20px}
.site-footer h5{color:var(--white);font-size:14px;font-weight:700;margin-bottom:12px}
.site-footer ul{list-style:none}
.social{display:flex;gap:10px}
.social span{width:34px;height:34px;background:#ddd}
.copyright{height:40px;background:var(--footer-deep);color:#999;font-size:12px;display:flex;align-items:center;justify-content:center}
</style>
</head>
<body>

<header class="site-header">
  <div class="brand"><span class="brand-mark"></span>MAREVIO</div>
  <nav class="main-nav">
    <a class="active">HOME</a><a>SERVICES</a><a>PRODUCTS</a><a>BLOG</a><a>ABOUT US</a><a>JOIN US</a><a>HELP &amp; SUPPORT</a>
  </nav>
</header>

<section class="hero">
  <div class="hero-photo" role="img" aria-label="Businessman in white shirt launching a paper plane against a blue sky"></div>
  <div class="hero-copy">
    <h2>WHY US</h2>
    <ul>
      <li><svg width="16" height="16" viewBox="0 0 16 16"><path d="M2 8l4 4 8-9" stroke="#fff" stroke-width="2.5" fill="none"/></svg>One stop service partner to boost your business in China and globally</li>
      <li><svg width="16" height="16" viewBox="0 0 16 16"><path d="M2 8l4 4 8-9" stroke="#fff" stroke-width="2.5" fill="none"/></svg>Experts in a variety of industries ready to help</li>
      <li><svg width="16" height="16" viewBox="0 0 16 16"><path d="M2 8l4 4 8-9" stroke="#fff" stroke-width="2.5" fill="none"/></svg>Professional and cost effective service</li>
      <li><svg width="16" height="16" viewBox="0 0 16 16"><path d="M2 8l4 4 8-9" stroke="#fff" stroke-width="2.5" fill="none"/></svg>Take care of your business carefully as if they are our own business</li>
    </ul>
  </div>
  <div class="slider-arrows">
    <span><svg width="10" height="12"><path d="M8 1L2 6l6 5" stroke="#fff" stroke-width="2" fill="none"/></svg></span>
    <span><svg width="10" height="12"><path d="M2 1l6 5-6 5" stroke="#fff" stroke-width="2" fill="none"/></svg></span>
  </div>
</section>

<section class="welcome">
  <h1 class="section-title">WELCOME TO <span class="accent">MAREVIO INTERNATIONAL</span></h1>
  <p>Established in China in 2008, Marevio International focuses on helping overseas small and medium-sized companies from all over the world to do business globally, especially in China. Our operations cover sourcing, import and export, legal services, translation, business development, market research and product inspection. Our services are provided by a team of professionals with long experience in their fields, who are committed to delivering results in line with the modern market. Quality, reliability and fair pricing are the values we share with every client, building lasting partnerships based on trust and mutual understanding, deep research and rigorous quality control.</p>
</section>

<section class="services">
  <h2 class="section-title">MAJOR <span class="accent">SERVICES</span></h2>
  <div class="service-grid">
    <div class="service">
      <div class="service-icon"><svg width="36" height="36" viewBox="0 0 36 36"><rect x="6" y="12" width="24" height="18" fill="#fff"/><path d="M6 12l12-7 12 7" fill="#fff"/></svg></div>
      <h3>IMPORT &amp; EXPORT</h3>
      <p>Lorem ipsum dolor sit amet, consectetur adipiscing elit, sed do eiusmod tempor incididunt ut labore et dolore.</p>
    </div>
    <div class="service">
      <div class="service-icon"><svg width="36" height="36" viewBox="0 0 36 36"><path d="M18 5v26M8 31h20M6 12h24" stroke="#fff" stroke-width="3"/><path d="M6 12l-4 9h8zM30 12l-4 9h8z" fill="#fff"/></svg></div>
      <h3>LEGAL SERVICE</h3>
      <p>Lorem ipsum dolor sit amet, consectetur adipiscing elit, sed do eiusmod tempor incididunt ut labore et dolore.</p>
    </div>
    <div class="service">
      <div class="service-icon"><svg width="36" height="36" viewBox="0 0 36 36"><circle cx="18" cy="12" r="7" fill="#fff"/><path d="M5 32c0-8 6-12 13-12s13 4 13 12z" fill="#fff"/></svg></div>
      <h3>TRANSLATION</h3>
      <p>Lorem ipsum dolor sit amet, consectetur adipiscing elit, sed do eiusmod tempor incididunt ut labore et dolore.</p>
    </div>
    <div class="service">
      <div class="service-icon"><svg width="36" height="36" viewBox="0 0 36 36"><circle cx="18" cy="18" r="12" stroke="#fff" stroke-width="5" fill="none"/><circle cx="18" cy="18" r="4" fill="#fff"/></svg></div>
      <h3>SOURCING</h3>
      <p>Lorem ipsum dolor sit amet, consectetur adipiscing elit, sed do eiusmod tempor incididunt ut labore et dolore.</p>
    </div>
    <div class="service">
      <div class="service-icon"><svg width="36" height="36" viewBox="0 0 36 36"><circle cx="14" cy="14" r="8" stroke="#fff" stroke-width="4" fill="none"/><circle cx="25" cy="25" r="6" stroke="#fff" stroke-width="4" fill="none"/></svg></div>
      <h3>BUSINESS DEVELOPMENT</h3>
      <p>Lorem ipsum dolor sit amet, consectetur adipiscing elit, sed do eiusmod tempor incididunt ut labore et dolore.</p>
    </div>
    <div class="service">
      <div class="service-icon"><svg width="36" height="36" viewBox="0 0 36 36"><circle cx="15" cy="15" r="9" stroke="#fff" stroke-width="4" fill="none"/><path d="M22 22l9 9" stroke="#fff" stroke-width="5"/></svg></div>
      <h3>MARKET RESEARCH</h3>
      <p>Lorem ipsum dolor sit amet, consectetur adipiscing elit, sed do eiusmod tempor incididunt ut labore et dolore.</p>
    </div>
  </div>
</section>

<section class="blog">
  <h2 class="section-title">LATEST <span class="accent">BLOG</span></h2>
  <div class="blog-grid">
    <article class="post">
      <div class="post-image" role="img" aria-label="Business people shaking hands in an office"><div class="post-date"><span class="day">02</span><span class="year">2016</span></div></div>
      <h4>Lorem ipsum dolor sit amet.</h4>
      <p>Lorem ipsum dolor sit amet, consectetur adipiscing elit. Integer nec odio praesent libero sed cursus ante dapibus diam.</p>
    </article>
    <article class="post">
      <div class="post-image" role="img" aria-label="Team meeting around a table with documents"><div class="post-date"><span class="day">02</span><span class="year">2016</span></div></div>
      <h4>Lorem ipsum dolor sit amet.</h4>
      <p>Lorem ipsum dolor sit amet, consectetur adipiscing elit. Integer nec odio praesent libero sed cursus ante dapibus diam.</p>
    </article>
    <article class="post">
      <div class="post-image" role="img" aria-label="Hands working on charts and a laptop"><div class="post-date"><span class="day">02</span><span class="year">2016</span></div></div>
      <h4>Lorem ipsum dolor sit amet.</h4>
      <p>Lorem ipsum dolor sit amet, consectetur adipiscing elit. Integer nec odio praesent libero sed cursus ante dapibus diam.</p>
    </article>
  </div>
</section>

<section class="feature">
  <div class="monitor">
    <div class="monitor-screen" role="img" aria-label="Office meeting shown on a desktop monitor screen"></div>
    <div class="monitor-stand"></div>
    <div class="monitor-base"></div>
  </div>
  <div class="feature-copy">
    <h2>LIST CERTAIN <span class="accent">SERVICES</span></h2>
    <p>Marevio is based in China and operates throughout the world. Our professionals are part of a network that spans continents, and we deliver an effective approach tailored to each client, from the first contact to the final result.</p>
    <p>We aim to be a one stop shop for all your commercial requirements and provide a wide range of services regardless of your sector. Marevio is based in China and operates throughout the world, and our team works closely with customers.</p>
    <span class="btn-outline">Read More</span>
  </div>
</section>

<section class="products">
  <h2 class="section-title">CATEGORY OF <span class="accent">PRODUCTS</span></h2>
  <p class="lead">Lorem ipsum dolor sit amet, consectetur adipiscing elit, sed do eiusmod tempor incididunt ut labore et dolore magna aliqua.</p>
  <div class="product-row">
    <div class="product" role="img" aria-label="Hand holding a smartphone"><span>NEQUE PORRO QUISQUAM</span></div>
    <div class="product" role="img" aria-label="Person reading on a tablet"><span>NEQUE PORRO QUISQUAM</span></div>
    <div class="product" role="img" aria-label="Hands typing on a laptop"><span>NEQUE PORRO QUISQUAM</span></div>
    <div class="product" role="img" aria-label="Laptop showing a news page"><span>NEQUE PORRO QUISQUAM</span></div>
  </div>
</section>

<section class="newsletter">
  <div class="newsletter-title">
    <h3>NEWSLETTERS SIGN UP</h3>
    <p>Sign up for our daily email by entering</p>
  </div>
  <div class="field">Name</div>
  <div class="field">Email Address</div>
  <div class="btn-submit">SUBMIT</div>
</section>

<section class="partners">
  <span>Kestrel</span><span>Lumora</span><span>Vantrix</span><span>Solvane</span><span>Verdal</span><span>Tarnis</span>
</section>

<footer class="site-footer">
  <div>
    <h5>MAREVIO</h5>
    <p>Lorem ipsum dolor sit amet, consectetur adipiscing elit. Sed do eiusmod tempor incididunt ut labore et dolore magna aliqua.</p>
    <p style="margin-top:10px">Ut enim ad minim veniam, quis nostrud exercitation ullamco laboris nisi ut aliquip.</p>
  </div>
  <div>
    <h5>LINKS</h5>
    <ul><li>What We Do</li><li>Who We Are</li><li>News and Insights</li><li>Careers</li><li>Contact Us</li></ul>
  </div>
  <div>
    <h5>GET IN TOUCH</h5>
    <ul><li>Address: 140 Harbor Lane, Suite 4</li><li>North Bridge City</li><li>Phone: 555-0148</li><li>Email: info@marevio.example</li></ul>
  </div>
  <div>
    <h5>SOCIAL MEDIA</h5>
    <div class="social"><span></span><span></span><span></span></div>
  </div>
</footer>
<div class="copyright">Copyright © 2016. All Rights Reserved.</div>

</body>
</html>
```